Silver Brook Constructions Ltd Stationary
business cards, stationary etc.
Silver Brook Constructions Ltd Stationary - Construction
Creative Brief
Simple
Dalton Wexford
4816 Ardmore Rd. Victoria B.C. V8N 4K7
250-384-6252 could we put this number under office instead of phone
222-222-2222 temporary until I get new number
dalton@silverbrookconstructions.example
www.silverbrookconstructions.example
We would like designs for business cards , envelopes, letterhead, thank-you cards with evelopes, fax cover sheet, and presentation folder. Thank you
information should be on the back of the card along with some clean lines and simplicity while keeping a very professional feel

```html
<!DOCTYPE html>
<html lang="en">
<head>
<meta charset="utf-8">
<title>Silver Brook Constructions Ltd — Business Cards</title>
<link href="https://fonts.googleapis.com/css2?family=Cinzel:wght@600&family=Montserrat:wght@400;500&display=swap" rel="stylesheet">
<style>
  :root{
    --backdrop:#3a3a3a;
    --card-dark:#050505;
    --card-light:#ffffff;
    --ink-light:#f2f2f2;
    --ink-dark:#1a1a1a;
    --green:#7aa63c;
    --caption:#eeeeee;
  }
  *{margin:0;padding:0;box-sizing:border-box}
  html,body{width:1200px;height:844px;overflow:hidden;background:var(--backdrop)}
  .sheet{position:relative;width:1200px;height:844px}
  .card{position:absolute;width:500px;height:306px;border-radius:16px;overflow:hidden}
  .card--dark{background:var(--card-dark);color:var(--ink-light)}
  .card--light{background:var(--card-light);color:var(--ink-dark)}
  .pos-front-left{left:77px;top:72px}
  .pos-front-right{left:625px;top:72px}
  .pos-back-left{left:77px;top:457px}
  .pos-back-right{left:625px;top:457px}

  .swoosh{position:absolute;left:0;top:0;width:500px;height:306px}

  .brand-disc{position:absolute;left:92px;top:22px;width:98px;height:98px;border-radius:50%;
    background:radial-gradient(circle at 50% 40%,#e8eee0 0%,#9fb78a 55%,#4d6b34 100%)}
  .brand-name{position:absolute;left:30px;top:146px;font-family:"Cinzel",serif;font-weight:600;line-height:1}
  .brand-name__main{display:block;font-size:30px;letter-spacing:1px}
  .brand-name__sub{display:block;font-size:12px;letter-spacing:2.4px;margin-top:4px}
  .card--dark .brand-name{color:var(--ink-light)}
  .card--light .brand-name{color:var(--ink-dark)}
  .tagline{position:absolute;left:31px;top:201px;font-family:"Montserrat",sans-serif;font-size:7.5px;
    letter-spacing:1.6px;color:var(--green);font-weight:500}
  .holder{position:absolute;right:28px;top:198px;font-family:"Cinzel",serif;font-size:14px;color:var(--green);letter-spacing:.5px}

  .mark-glow{position:absolute;left:160px;top:22px;width:180px;height:190px;border-radius:50%}
  .card--dark .mark-glow{background:radial-gradient(ellipse at 50% 45%,rgba(220,228,230,.75) 0%,rgba(120,130,132,.35) 45%,rgba(0,0,0,0) 72%)}
  .card--light .mark-glow{background:radial-gradient(ellipse at 50% 45%,rgba(110,118,120,.8) 0%,rgba(150,156,158,.35) 45%,rgba(255,255,255,0) 72%)}

  .contact{position:absolute;left:50px;font-family:"Montserrat",sans-serif;font-size:9.5px;white-space:nowrap;display:flex;gap:14px;align-items:center}
  .contact--top{top:246px}
  .contact--bottom{top:264px}
  .card--dark .contact{color:#d8d8d8}
  .card--light .contact{color:#333}
  .contact__item{display:inline-flex;align-items:center;gap:4px}
  .icon{width:9px;height:9px;fill:var(--green)}

  .caption{position:absolute;width:500px;text-align:center;font-family:"Montserrat",sans-serif;font-weight:400;
    font-size:21px;letter-spacing:2.5px;font-variant:small-caps;color:var(--caption)}
  .caption--front-left{left:77px;top:384px}
  .caption--front-right{left:625px;top:384px}
  .caption--back-left{left:77px;top:770px}
  .caption--back-right{left:625px;top:770px}
</style>
</head>
<body>
<main class="sheet">

  <section class="card card--dark pos-front-left">
    <div class="brand-disc"></div>
    <div class="brand-name"><span class="brand-name__main">SILVER BROOK</span><span class="brand-name__sub">CONSTRUCTIONS LTD.</span></div>
    <div class="tagline">BUILT WELL, BUILT TO LAST</div>
    <div class="holder">DALTON WEXFORD</div>
    <svg class="swoosh" viewBox="0 0 500 306" aria-hidden="true">
      <defs>
        <linearGradient id="silverDark" x1="0" x2="1"><stop offset="0" stop-color="#555"/><stop offset=".5" stop-color="#d9dcdd"/><stop offset="1" stop-color="#777"/></linearGradient>
        <linearGradient id="greenDark" x1="0" x2="1"><stop offset="0" stop-color="#3e6316"/><stop offset=".5" stop-color="#9cc75a"/><stop offset="1" stop-color="#4f7a1f"/></linearGradient>
      </defs>
      <path d="M0 236 C130 212 320 214 500 228 L500 236 C320 226 140 228 0 256 Z" fill="url(#silverDark)"/>
      <path d="M0 260 C120 230 300 234 500 246 L500 262 C300 250 140 254 0 290 Z" fill="url(#greenDark)"/>
    </svg>
  </section>

  <section class="card card--light pos-front-right">
    <div class="brand-disc"></div>
    <div class="brand-name"><span class="brand-name__main">SILVER BROOK</span><span class="brand-name__sub">CONSTRUCTIONS LTD.</span></div>
    <div class="tagline">BUILT WELL, BUILT TO LAST</div>
    <div class="holder">DALTON WEXFORD</div>
    <svg class="swoosh" viewBox="0 0 500 306" aria-hidden="true">
      <defs>
        <linearGradient id="silverLight" x1="0" x2="1"><stop offset="0" stop-color="#9a9d9e"/><stop offset=".5" stop-color="#e4e6e7"/><stop offset="1" stop-color="#8a8e8f"/></linearGradient>
        <linearGradient id="greenLight" x1="0" x2="1"><stop offset="0" stop-color="#3e6316"/><stop offset=".5" stop-color="#9cc75a"/><stop offset="1" stop-color="#4f7a1f"/></linearGradient>
      </defs>
      <path d="M0 236 C130 212 320 214 500 228 L500 236 C320 226 140 228 0 256 Z" fill="url(#silverLight)"/>
      <path d="M0 260 C120 230 300 234 500 246 L500 262 C300 250 140 254 0 290 Z" fill="url(#greenLight)"/>
    </svg>
  </section>

  <section class="card card--dark pos-back-left">
    <div class="mark-glow" role="img" aria-label="Large faint brand emblem area in silver tones"></div>
    <div class="contact contact--top">
      <span class="contact__item"><svg class="icon" viewBox="0 0 10 10"><path d="M2 0.5 L3.6 2.8 L2.7 3.8 C3.3 5.2 4.8 6.7 6.2 7.3 L7.2 6.4 L9.5 8 L8.4 9.5 C4.5 9.3 0.7 5.5 0.5 1.6 Z"/></svg>250-384-6252</span>
      <span class="contact__item"><svg class="icon" viewBox="0 0 10 10"><path d="M2 0.5 L3.6 2.8 L2.7 3.8 C3.3 5.2 4.8 6.7 6.2 7.3 L7.2 6.4 L9.5 8 L8.4 9.5 C4.5 9.3 0.7 5.5 0.5 1.6 Z"/></svg>250-217-9043</span>
      <span class="contact__item"><svg class="icon" viewBox="0 0 10 10"><rect x="0.5" y="2" width="9" height="6"/></svg>dalton@silverbrookconstructions.example</span>
    </div>
    <div class="contact contact--bottom">
      <span class="contact__item"><svg class="icon" viewBox="0 0 10 10"><circle cx="5" cy="5" r="4.5"/></svg>www.silverbrookconstructions.example</span>
      <span class="contact__item"><svg class="icon" viewBox="0 0 10 10"><path d="M5 0.5 C2.5 0.5 1.5 2.3 1.5 3.8 C1.5 6 5 9.5 5 9.5 C5 9.5 8.5 6 8.5 3.8 C8.5 2.3 7.5 0.5 5 0.5 Z"/></svg>4816 Ardmore Rd. Victoria B.C. V8N 4K7</span>
    </div>
  </section>

  <section class="card card--light pos-back-right">
    <div class="mark-glow" role="img" aria-label="Large faint brand emblem area in grey tones"></div>
    <div class="contact contact--top">
      <span class="contact__item"><svg class="icon" viewBox="0 0 10 10"><path d="M2 0.5 L3.6 2.8 L2.7 3.8 C3.3 5.2 4.8 6.7 6.2 7.3 L7.2 6.4 L9.5 8 L8.4 9.5 C4.5 9.3 0.7 5.5 0.5 1.6 Z"/></svg>250-384-6252</span>
      <span class="contact__item"><svg class="icon" viewBox="0 0 10 10"><path d="M2 0.5 L3.6 2.8 L2.7 3.8 C3.3 5.2 4.8 6.7 6.2 7.3 L7.2 6.4 L9.5 8 L8.4 9.5 C4.5 9.3 0.7 5.5 0.5 1.6 Z"/></svg>250-217-9043</span>
      <span class="contact__item"><svg class="icon" viewBox="0 0 10 10"><rect x="0.5" y="2" width="9" height="6"/></svg>dalton@silverbrookconstructions.example</span>
    </div>
    <div class="contact contact--bottom">
      <span class="contact__item"><svg class="icon" viewBox="0 0 10 10"><circle cx="5" cy="5" r="4.5"/></svg>www.silverbrookconstructions.example</span>
      <span class="contact__item"><svg class="icon" viewBox="0 0 10 10"><path d="M5 0.5 C2.5 0.5 1.5 2.3 1.5 3.8 C1.5 6 5 9.5 5 9.5 C5 9.5 8.5 6 8.5 3.8 C8.5 2.3 7.5 0.5 5 0.5 Z"/></svg>4816 Ardmore Rd. Victoria B.C. V8N 4K7</span>
    </div>
  </section>

  <p class="caption caption--front-left">Business Card Front</p>
  <p class="caption caption--front-right">Business Card Front</p>
  <p class="caption caption--back-left">Business Card Back</p>
  <p class="caption caption--back-right">Business Card Back</p>

</main>
</body>
</html>
```